Business Strategy Company
Cards & Paper for Enterprise Collaboration Data Company
Project: Business Strategy Company
Business Strategy Company -
Creative Brief
Professional
Tobin G. Maraselt
CEO
31927 Harrowgate Ave. Suite 400 Berkley, CA 90388
tobin@quandelrox.example
www.quandelrox.example
Please include tagline: "Collective Work Insight" We would like a clean, modern card like the types found in these designs: https://www.pendlewick.example/drafts/display/contest/93587/draft/705568 https://www.pendlewick.example/drafts/display/contest/79787/draft/600578 https://www.pendlewick.example/drafts/display/contest/77433/draft/650842 https://www.pendlewick.example/drafts/display/contest/50102/draft/406651 https://www.pendlewick.example/drafts/display/contest/101628/draft/769948 https://www.pendlewick.example/drafts/display/contest/101641/draft/771307 https://www.pendlewick.example/drafts/display/contest/99022/draft/771303
We like a field of dark color or a gradient with the logo in either white or a color just slightly lighter/darker than the background (i.e. if the background is black, the logo would either be white or very dark gray). We'd like to see both.

```html
<!DOCTYPE html>
<html lang="en">
<head>
<meta charset="utf-8">
<title>quandelrox — Stationery</title>
<link href="https://fonts.googleapis.com/css2?family=Exo+2:wght@400;600;700&display=swap" rel="stylesheet">
<style>
  :root{
    --bg:#e6e4e1;
    --paper:#ffffff;
    --ink-navy:#1f2a5c;
    --ink-cyan:#3fbfd8;
    --ink-grey:#6b6f7c;
    --faint:#d9dbe3;
    --card-dark:#3a3b3f;
    --shadow:0 6px 18px rgba(0,0,0,.18);
  }
  *{box-sizing:border-box;margin:0;padding:0}
  html,body{width:1200px;height:913px;overflow:hidden}
  body{background:var(--bg);font-family:"Exo 2",sans-serif;color:var(--ink-grey);position:relative}

  .wordmark{display:flex;align-items:center;gap:6px;font-weight:600;color:var(--ink-navy);letter-spacing:.02em;white-space:nowrap}
  .wordmark .dot{display:inline-block;border-radius:50%;background:var(--ink-cyan)}
  .faint-block{position:absolute;background:var(--faint);border-radius:10%}

  /* Letterhead */
  .letterhead{position:absolute;left:90px;top:250px;width:420px;height:560px;background:var(--paper);box-shadow:var(--shadow);overflow:hidden}
  .letterhead .wordmark{position:absolute;left:34px;top:40px;font-size:22px}
  .letterhead .wordmark .dot{width:14px;height:14px}
  .letterhead .faint-block{right:40px;top:230px;width:120px;height:120px}
  .letterhead .contact{position:absolute;left:34px;bottom:34px;font-size:9px;line-height:1.55}

  /* Business card front */
  .card-front{position:absolute;left:560px;top:220px;width:270px;height:160px;background:var(--paper);border-radius:8px;box-shadow:var(--shadow);overflow:hidden}
  .card-front .wordmark{position:absolute;left:18px;top:18px;font-size:15px}
  .card-front .wordmark .dot{width:10px;height:10px}
  .card-front .faint-block{right:18px;top:16px;width:52px;height:52px}
  .card-front .person{position:absolute;left:18px;top:72px}
  .card-front .person-name{font-size:13px;font-weight:700;color:var(--ink-navy)}
  .card-front .person-title{font-size:9px;color:var(--ink-grey)}
  .card-front .details{position:absolute;left:18px;bottom:12px;font-size:7.5px;line-height:1.5;list-style:none}
  .card-front .details li{white-space:nowrap}
  .card-front .details li::before{content:"";display:inline-block;width:5px;height:5px;background:var(--ink-cyan);margin-right:5px}

  /* Business card back */
  .card-back{position:absolute;left:870px;top:90px;width:270px;height:160px;background:var(--card-dark);border-radius:8px;box-shadow:var(--shadow);display:flex;flex-direction:column;align-items:center;justify-content:center;gap:8px}
  .card-back .wordmark{color:#fff;font-size:18px}
  .card-back .wordmark .dot{width:11px;height:11px;background:#fff}
  .card-back .tagline{color:#fff;font-size:10px;letter-spacing:.08em}

  /* Envelope */
  .envelope{position:absolute;left:610px;top:440px;width:520px;height:250px;background:var(--paper);box-shadow:var(--shadow);overflow:hidden}
  .envelope .flap-line{position:absolute;inset:0}
  .envelope .wordmark{position:absolute;left:28px;top:150px;font-size:17px}
  .envelope .wordmark .dot{width:11px;height:11px}
  .envelope .return-address{position:absolute;left:28px;top:180px;font-size:8px;line-height:1.5}
  .envelope .faint-block{right:60px;top:80px;width:80px;height:80px}
</style>
</head>
<body>

<section class="letterhead" aria-label="Letterhead">
  <div class="wordmark"><span class="dot"></span>quandelrox</div>
  <div class="faint-block" aria-hidden="true"></div>
  <div class="contact">
    31927 Harrowgate Ave. Suite 400<br>
    Berkley, CA 90388<br>
    T 555.014.2270 &nbsp; F 555.014.2271<br>
    tobin@quandelrox.example<br>
    www.quandelrox.example
  </div>
</section>

<section class="card-front" aria-label="Business card front">
  <div class="wordmark"><span class="dot"></span>quandelrox</div>
  <div class="faint-block" aria-hidden="true"></div>
  <div class="person">
    <div class="person-name">Tobin G. Maraselt</div>
    <div class="person-title">CEO</div>
  </div>
  <ul class="details">
    <li>31927 Harrowgate Ave. Suite 400 Berkley, CA 90388</li>
    <li>tobin@quandelrox.example</li>
    <li>www.quandelrox.example</li>
  </ul>
</section>

<section class="card-back" aria-label="Business card back">
  <div class="wordmark"><span class="dot"></span>quandelrox</div>
  <div class="tagline">Collective Work Insight</div>
</section>

<section class="envelope" aria-label="Envelope">
  <svg class="flap-line" width="520" height="250" viewBox="0 0 520 250" aria-hidden="true">
    <polyline points="0,0 260,120 520,0" fill="none" stroke="#e3e4e8" stroke-width="1.5"/>
  </svg>
  <div class="faint-block" aria-hidden="true"></div>
  <div class="wordmark"><span class="dot"></span>quandelrox</div>
  <div class="return-address">
    31927 Harrowgate Ave. Suite 400<br>
    Berkley, CA 90388
  </div>
</section>

</body>
</html>
```